TV+Music+Social Network+Entertainment+yellowpages= Designers lol

TV+ Music+ Social Network +Entertainment+ yellowpages=

ZAVQUEL.COM

Zavquel is a one-stop shop promotional plateform that will communicate information to all user of what is COOL, NEW and Exicting in your Neighborhood.(News,Events,Entertainment,ect) We promote for all User/Entrepreneur/business/Talents.We are the future and dream destination for all to whom owns a computer. Forming the the World Wide Web into your Local Wide Web. (Atlanta, Dallas, Las Vegas, New York ect.)

* EX: ( WWW. ??? .com =LWW. ??? .com)
WORLD = LOCAL

* Goal/Mission: Have customer/user visit the website and then leave their house to go experience life in their respective surroundings.

/////////////////////////Web page///////////////////////

Colors:Blue/Green/black

include: interchangable background picture @ top (to update easily and keep fresh) On this background picture include logo (top left) login/sign (top left)

Major Tabs: Music/Daylife/Nightlife/Video/Shop

• Tv screen/search engine

```html
<!DOCTYPE html>
<html lang="en">
<head>
<meta charset="utf-8">
<title>Zavquel</title>
<link rel="stylesheet" href="https://fonts.googleapis.com/css2?family=Arimo:wght@400;700&family=Signika:wght@400;600&display=swap">
<style>
:root{
  --black:#000;
  --blue:#1d6fc9;
  --blue-dark:#0c4f9e;
  --blue-light:#3c8fe0;
  --green:#8fcf2f;
  --green-dark:#6aad17;
  --page:#efefef;
  --panel:#f4f4f4;
  --border:#d4d4d4;
  --text:#222;
  --muted:#555;
  --link:#1a5aa6;
  --star:#1b4fb5;
  --star-off:#b5b5b5;
  --footer:#e2e2e2;
}
*{box-sizing:border-box;margin:0;padding:0}
html,body{width:873px;height:1200px;overflow:hidden}
body{background:var(--page);font-family:"Arimo",Arial,sans-serif;color:var(--text);position:relative}
.abs{position:absolute}

.site-header{position:absolute;left:0;top:0;width:873px;height:92px;background:var(--black)}
.brand{position:absolute;left:22px;top:22px;display:flex;align-items:center;gap:10px}
.brand-dot{width:44px;height:44px;border-radius:50%;background:linear-gradient(135deg,#3c8fe0,#0c4f9e)}
.brand-name{font-family:"Signika",sans-serif;font-weight:400;font-size:34px;color:#fff;letter-spacing:.5px}
.search{position:absolute;left:713px;top:23px;display:flex}
.search-field{width:136px;height:21px;background:linear-gradient(#3c8fe0,#1a5fb8);border-radius:3px 0 0 3px;color:#fff;font-size:11px;font-weight:700;padding:4px 6px}
.search-btn{width:21px;height:21px;background:var(--green);border-radius:0 3px 3px 0;display:flex;align-items:center;justify-content:center}
.account{position:absolute;right:8px;top:64px;font-size:12px;font-weight:700;color:#a9a9a9;word-spacing:1px}
.account span.sep{margin:0 6px;font-weight:400}

.main-nav{position:absolute;left:0;top:92px;width:873px;height:35px;background:linear-gradient(var(--blue-light),var(--blue-dark));display:flex}
.main-nav a{display:block;height:35px;line-height:35px;padding:0 15px;color:#fff;font-size:12px;font-weight:700;text-decoration:none;border-right:1px solid rgba(255,255,255,.18)}
.main-nav a.active{background:var(--green);color:#173b00;padding:0 15px 0 12px}

.panel{position:absolute;background:var(--panel);border:1px solid var(--border);border-radius:4px;overflow:hidden}
.panel-head{height:43px;background:linear-gradient(var(--blue-light),var(--blue-dark));color:#fff;font-family:"Signika",sans-serif;font-size:18px;font-weight:400;padding:11px 13px}
.panel-head.green{background:linear-gradient(#a8dd55,var(--green-dark));display:flex;align-items:center;gap:9px}

.media{position:absolute;width:124px}
.thumb{border:1px solid #c9c9c9;background:#fff;padding:3px;position:relative}
.thumb .fill{height:72px;background:linear-gradient(135deg,#8a7a5c,#c9b08a 55%,#6f6a58)}
.thumb .plus{position:absolute;left:6px;bottom:6px;width:12px;height:12px;background:#ccc;border:1px solid #fff}
.media h3{margin-top:10px;font-size:12px;font-weight:700;color:var(--link)}
.media p{font-size:12px;font-weight:700;color:#111;line-height:15px}
.stars{letter-spacing:1px;font-size:13px}
.stars .on{color:var(--star)}
.stars .off{color:var(--star-off)}
.media.small{width:100px}
.media.small .thumb .fill{height:58px;background:linear-gradient(#f2f2f2,#d8d8d8)}
.media.small h3,.media.small p{font-size:11px;line-height:14px}

.next{position:absolute;width:0;height:0;border-top:9px solid transparent;border-bottom:9px solid transparent;border-left:14px solid #3c8fe0}
.btns{position:absolute;display:flex;gap:5px}
.btn{height:21px;padding:0 8px;line-height:21px;background:linear-gradient(#a8dd55,var(--green-dark));color:#fff;font-size:11px;font-weight:700;border-radius:2px}

.games-title{position:absolute;left:0;width:100%;text-align:center;color:var(--green-dark);font-family:"Signika",sans-serif;font-size:14px;font-weight:600}
.intro{position:absolute;left:15px;width:530px;font-size:10.5px;line-height:15px;color:var(--muted)}
.game{position:absolute;width:89px;height:90px;border:1px solid #c9c9c9;background:#fff;padding:2px}
.game div{width:100%;height:100%}

.feature-screen{position:absolute;left:594px;top:196px;width:261px;height:228px;background:linear-gradient(160deg,#1c2f6d,#3b3f55 50%,#121a33)}
.player-bar{position:absolute;left:594px;top:424px;width:261px;height:20px;background:#2a2a2a;display:flex;align-items:center;gap:6px;padding:0 7px;font-size:8px;color:#aaa}
.player-track{flex:1;height:3px;background:#555;position:relative}
.player-track i{position:absolute;left:0;top:0;width:40%;height:3px;background:#bbb}
.feature-meta{position:absolute;left:594px;top:444px;width:261px;height:28px;background:#dcdcdc}
.feature-title{position:absolute;left:605px;top:430px;font-family:"Signika",sans-serif;font-size:15px;font-weight:600;color:var(--blue-dark)}
.feature-by{position:absolute;left:605px;top:453px;font-size:10px;color:var(--muted)}
.feature-stars{position:absolute;left:770px;top:450px;font-size:14px}

.social{position:absolute;top:501px;height:34px;background:linear-gradient(#fff,#e6e6e6);border:1px solid #c8c8c8;border-radius:3px;display:flex;align-items:center;gap:6px;padding:0 6px;font-size:9px;color:#666;line-height:10px}
.social b{display:block;font-size:11px;color:var(--link)}
.social .sq{width:20px;height:20px;background:var(--blue-dark);flex:none}
.social.feed .sq{background:#f08a1c}
.social.feed{font-size:15px;font-weight:700;color:#f08a1c}

.fans{position:absolute;left:595px;top:562px;width:260px;height:235px;background:#fff;border:1px solid #8ea1c9}
.fans-head{height:24px;background:#3b5ba0;color:#fff;font-size:15px;font-weight:700;padding:3px 6px}
.fans-page{position:absolute;left:6px;top:31px;display:flex;gap:9px}
.fans-page .av{width:38px;height:38px;background:linear-gradient(135deg,#1e3a6b,#4d7ab3)}
.fans-page .nm{font-size:12px;color:var(--link);font-weight:700}
.like{margin-top:4px;width:38px;height:17px;border:1px solid #c0c7d6;background:#eef0f5;font-size:10px;color:#3b5ba0;padding:2px 4px}
.fans-line{position:absolute;left:6px;top:83px;width:246px;border-top:1px solid #dde0e8;padding-top:7px;font-size:9px;color:#333}
.faces{position:absolute;left:7px;top:108px;display:grid;grid-template-columns:repeat(5,44px);column-gap:5px;row-gap:4px}
.face{text-align:center;font-size:8px;color:#555}
.face div{width:42px;height:42px;margin:0 auto 3px;background:linear-gradient(#9c8673,#5c4a3e)}

.site-footer{position:absolute;left:0;top:1133px;width:873px;height:67px;background:var(--footer);text-align:center;font-size:11px}
.site-footer .links{margin-top:16px;color:var(--link)}
.site-footer .copy{margin-top:9px;color:var(--muted)}
</style>
</head>
<body>

<header class="site-header">
  <div class="brand"><div class="brand-dot"></div><div class="brand-name">zavquel</div></div>
  <div class="search">
    <div class="search-field">Search</div>
    <div class="search-btn">
      <svg width="12" height="12" viewBox="0 0 12 12"><circle cx="5" cy="5" r="3.3" fill="none" stroke="#1d4d00" stroke-width="1.6"/><line x1="7.5" y1="7.5" x2="11" y2="11" stroke="#1d4d00" stroke-width="1.8"/></svg>
    </div>
  </div>
  <div class="account">Sign Up<span class="sep">|</span>Quicklist (0)<span class="sep">|</span>Help<span class="sep">|</span>Log In</div>
</header>

<nav class="main-nav">
  <a class="active" href="#">Home</a><a href="#">Music</a><a href="#">Daylife</a><a href="#">Nightlife</a><a href="#">Video</a><a href="#">Shop</a>
</nav>

<!-- Featured videos -->
<section class="panel" style="left:17px;top:144px;width:560px;height:274px">
  <h2 class="panel-head">Featured Funny Videos</h2>
  <div class="media" style="left:55px;top:73px">
    <div class="thumb"><div class="fill" role="img" aria-label="Video still of people at a party"></div><span class="plus"></span></div>
    <h3>Funny Bahamas...</h3><p>Added by: pelvo</p><p>Views: 19,532</p>
    <p>3m:50s <span class="stars"><span class="on">★★</span><span class="off">★★★</span></span></p>
  </div>
  <div class="media" style="left:216px;top:73px">
    <div class="thumb"><div class="fill" role="img" aria-label="Video still of people at a party"></div><span class="plus"></span></div>
    <h3>Funny Bahamas...</h3><p>Added by: pelvo</p><p>Views: 19,532</p>
    <p>3m:50s <span class="stars"><span class="on">★★</span><span class="off">★★★</span></span></p>
  </div>
  <div class="media" style="left:377px;top:73px">
    <div class="thumb"><div class="fill" role="img" aria-label="Video still of people at a party"></div><span class="plus"></span></div>
    <h3>Funny Bahamas...</h3><p>Added by: pelvo</p><p>Views: 19,532</p>
    <p>3m:50s <span class="stars"><span class="on">★★</span><span class="off">★★★</span></span></p>
  </div>
  <span class="next" style="left:536px;top:134px"></span>
  <div class="btns" style="left:460px;top:236px"><span class="btn">More</span><span class="btn">Less</span></div>
</section>

<!-- Featured images -->
<section class="panel" style="left:17px;top:436px;width:560px;height:382px">
  <h2 class="panel-head">Featured Funny Images</h2>
  <div class="games-title" style="top:58px">Play Free Online Games - Latest Funny Games</div>
  <p class="intro" style="top:85px">Lorem Ipsum is simply dummy text of the printing and typesetting industry. Lorem Ipsum has been the industry's standard, remaining essentially unchanged. It was popularised in the 1960s with the release of Dryprint sheets containing Lorem Ipsum passages, and more recently with desktop publishing software like Quillset Layout including versions of Lorem Ipsum.</p>
  <div class="game" style="left:17px;top:167px"><div role="img" aria-label="Cartoon girl game art" style="background:linear-gradient(#fbf27a,#f5b9c9)"></div></div>
  <div class="game" style="left:126px;top:167px"><div role="img" aria-label="Flying penguin game art" style="background:linear-gradient(#1d2f7a,#5a8fd6)"></div></div>
  <div class="game" style="left:234px;top:167px"><div role="img" aria-label="Red sports car game art" style="background:linear-gradient(#2a0a0a,#b0201a)"></div></div>
  <div class="game" style="left:342px;top:167px"><div role="img" aria-label="Silver sports car game art" style="background:linear-gradient(#e8ecec,#8aa09c)"></div></div>
  <div class="game" style="left:450px;top:167px"><div role="img" aria-label="Dress-up game art" style="background:linear-gradient(#f5f0a0,#a6c96a)"></div></div>
  <div class="game" style="left:17px;top:273px"><div role="img" aria-label="Candy world game art" style="background:linear-gradient(#f06ab5,#4aa3e6)"></div></div>
  <div class="game" style="left:126px;top:273px"><div role="img" aria-label="Forest animal game art" style="background:linear-gradient(#4c3a24,#7a5a33)"></div></div>
  <div class="game" style="left:234px;top:273px"><div role="img" aria-label="Bubble puzzle game art" style="background:linear-gradient(#2236c9,#5b3ad6)"></div></div>
  <div class="game" style="left:342px;top:273px"><div role="img" aria-label="Fashion dress-up game art" style="background:linear-gradient(#f2e0e4,#e08ab0)"></div></div>
  <div class="game" style="left:450px;top:273px"><div role="img" aria-label="Concept car game art" style="background:linear-gradient(#f4f4f4,#555)"></div></div>
</section>

<!-- Featured videos (audio) -->
<section class="panel" style="left:17px;top:837px;width:560px;height:269px">
  <h2 class="panel-head">Featured Funny Videos</h2>
  <div class="media small" style="left:45px;top:67px">
    <div class="thumb"><div class="fill" role="img" aria-label="Speaker and music note icon"></div><span class="plus"></span></div>
    <h3>Funny Bahamas...</h3><p>Added by: pelvo</p><p>Views: 19,532</p>
    <p>3m:50s <span class="stars"><span class="on">★★</span><span class="off">★★★</span></span></p>
  </div>
  <div class="media small" style="left:167px;top:67px">
    <div class="thumb"><div class="fill" role="img" aria-label="Speaker and music note icon"></div><span class="plus"></span></div>
    <h3>Funny Bahamas...</h3><p>Added by: pelvo</p><p>Views: 19,532</p>
    <p>3m:50s <span class="stars"><span class="on">★★</span><span class="off">★★★</span></span></p>
  </div>
  <div class="media small" style="left:290px;top:67px">
    <div class="thumb"><div class="fill" role="img" aria-label="Speaker and music note icon"></div><span class="plus"></span></div>
    <h3>Funny Bahamas...</h3><p>Added by: pelvo</p><p>Views: 19,532</p>
    <p>3m:50s <span class="stars"><span class="on">★★</span><span class="off">★★★</span></span></p>
  </div>
  <div class="media small" style="left:413px;top:67px">
    <div class="thumb"><div class="fill" role="img" aria-label="Speaker and music note icon"></div><span class="plus"></span></div>
    <h3>Funny Bahamas...</h3><p>Added by: pelvo</p><p>Views: 19,532</p>
    <p>3m:50s <span class="stars"><span class="on">★★</span><span class="off">★★★</span></span></p>
  </div>
  <span class="next" style="left:534px;top:135px"></span>
  <div class="btns" style="left:460px;top:231px"><span class="btn">More</span><span class="btn">Less</span></div>
</section>

<!-- Today's feature -->
<section class="panel" style="left:593px;top:144px;width:262px;height:43px;border:none">
  <h2 class="panel-head green">
    <svg width="20" height="20" viewBox="0 0 20 20"><circle cx="10" cy="10" r="9" fill="#fff"/><path d="M10 4v9M6 9.5l4 4 4-4" stroke="#6aad17" stroke-width="2.2" fill="none"/></svg>
    Today's Feature
  </h2>
</section>
<div class="feature-screen" role="img" aria-label="Featured news video still: a speaker at a podium"></div>
<div class="player-bar">
  <svg width="7" height="8" viewBox="0 0 7 8"><path d="M0 0l7 4-7 4z" fill="#ccc"/></svg>
  <svg width="6" height="6" viewBox="0 0 6 6"><rect width="6" height="6" fill="#ccc"/></svg>
  <div class="player-track"><i></i></div>
  <span>00:00/00:00</span>
</div>
<div class="feature-meta"></div>
<div class="abs" style="left:594px;top:424px;width:261px;height:48px;background:#dcdcdc"></div>
<div class="feature-title">Prank Gone Extremely Wrong</div>
<div class="feature-by">Added by: sorrel , 11 day(s) ago</div>
<div class="feature-stars stars"><span class="on">★★</span><span class="off">★★★</span></div>

<div class="social" style="left:596px;width:80px"><span class="sq"></span><span>Find us on<b>Friendloop</b></span></div>
<div class="social" style="left:684px;width:83px"><span class="sq" style="background:#3aa7e0"></span><span>Find us on<b>Chirpline</b></span></div>
<div class="social feed" style="left:775px;width:80px"><span class="sq"></span>Feed</div>

<aside class="fans">
  <div class="fans-head">friendloop</div>
  <div class="fans-page">
    <div class="av" role="img" aria-label="Page avatar"></div>
    <div><div class="nm">skyla</div><div class="like">Like</div></div>
  </div>
  <div class="fans-line">4,157 people like skyla</div>
  <div class="faces">
    <div class="face"><div role="img" aria-label="Fan avatar"></div>Aurel</div>
    <div class="face"><div role="img" aria-label="Fan avatar"></div>Stellan</div>
    <div class="face"><div role="img" aria-label="Fan avatar"></div>Mirela</div>
    <div class="face"><div role="img" aria-label="Fan avatar"></div>Tansy</div>
    <div class="face"><div role="img" aria-label="Fan avatar"></div>Niko</div>
    <div class="face"><div role="img" aria-label="Fan avatar"></div>Joran</div>
    <div class="face"><div role="img" aria-label="Fan avatar"></div>Zebulon</div>
    <div class="face"><div role="img" aria-label="Fan avatar"></div>Anika</div>
    <div class="face"><div role="img" aria-label="Fan avatar"></div>Jasper</div>
    <div class="face"><div role="img" aria-label="Fan avatar"></div>Tobin</div>
  </div>
</aside>

<footer class="site-footer">
  <div class="links">Privacy Policy &nbsp;|&nbsp; Site User Terms and Conditions</div>
  <div class="copy">Copyright 2009-2010 © zavquel.com. All Rights Reserved.</div>
</footer>

</body>
</html>
```